Road Construction Company needs business cards

We would like a new business card designed for our business.

We're a road construction company based in Qld, Australia.

Can the business card please have the following information on it.

Name: Brent Malvoy
Position: General Manager
Phone: 0471 592 304
Email: Brent.malvoy@quendix.com.au
Address: 87 Harrowgate Ave, Pindarra, QLD, 4000
Website: www.quendix.com.au

Visually we'd like the card to be professional and simple.

Attached is our logo.

Our website is www.quendix.com.au

Target Market(s)

Men aged 25-60

Contact Information for Business Card

As listed in project description

Font styles to use
Serif

Requirements
Must have
• Large logo on back of card

```html
<!DOCTYPE html>
<html lang="en">
<head>
<meta charset="utf-8">
<title>Quendix Business Card</title>
<link href="https://fonts.googleapis.com/css2?family=Poppins:wght@300;700&family=Roboto+Condensed:wght@700&display=swap" rel="stylesheet">
<style>
  :root {
    --page: #d9d9d9;
    --card: #141414;
    --white: #ffffff;
    --blue: #2ba3dd;
    --grey-light: #cfcfcf;
    --photo-mid: #2a2a2a;
    --photo-edge: #141414;
  }
  * { margin: 0; padding: 0; box-sizing: border-box; }
  html, body {
    width: 1200px; height: 846px; overflow: hidden;
    background: var(--page);
  }
  .sheet {
    position: relative; width: 1200px; height: 846px;
    display: flex; align-items: center; justify-content: center; gap: 24px;
  }
  .card {
    position: relative; width: 560px; height: 320px;
    background: var(--card); overflow: hidden;
    box-shadow: 0 10px 24px rgba(0,0,0,0.18);
  }
  /* front */
  .card-front .machine-photo {
    position: absolute; right: 0; top: 0; width: 290px; height: 320px;
    background: radial-gradient(ellipse 55% 45% at 55% 42%, var(--photo-mid), var(--photo-edge) 75%);
  }
  .brand {
    position: absolute; display: flex; align-items: center; gap: 10px;
    font-family: "Poppins", sans-serif; font-weight: 700; color: var(--white);
    letter-spacing: 0.04em;
  }
  .card-front .brand { left: 34px; top: 34px; font-size: 38px; line-height: 1; }
  .brand-square { width: 12px; height: 12px; background: var(--blue); }
  .person { position: absolute; left: 52px; top: 104px; font-family: "Poppins", sans-serif; }
  .person-name { font-weight: 700; font-size: 28px; color: var(--blue); line-height: 1.1; }
  .person-role { font-weight: 300; font-size: 14px; color: var(--grey-light); margin-top: 2px; }
  .contacts {
    position: absolute; left: 52px; top: 180px; list-style: none;
    font-family: "Roboto Condensed", sans-serif; font-weight: 700;
    font-size: 17px; color: var(--white); line-height: 1.15;
  }
  .contacts li { display: flex; align-items: flex-start; gap: 12px; margin-bottom: 6px; }
  .contacts svg { width: 18px; height: 18px; flex: none; fill: var(--blue); margin-top: 1px; }
  /* back */
  .card-back { display: flex; align-items: center; justify-content: center; }
  .card-back .brand { position: static; font-size: 72px; gap: 18px; }
  .card-back .brand-square { width: 22px; height: 22px; }
</style>
</head>
<body>
<main class="sheet">
  <section class="card card-front">
    <div class="machine-photo" role="img" aria-label="Dark studio photograph of a road roller compactor"></div>
    <div class="brand"><span class="brand-square"></span>QUENDIX</div>
    <div class="person">
      <p class="person-name">Brent Malvoy</p>
      <p class="person-role">General Manager</p>
    </div>
    <ul class="contacts">
      <li>
        <svg viewBox="0 0 24 24"><path d="M6.6 10.8a15.1 15.1 0 0 0 6.6 6.6l2.2-2.2a1 1 0 0 1 1-.25 11.4 11.4 0 0 0 3.6.57 1 1 0 0 1 1 1V20a1 1 0 0 1-1 1A17 17 0 0 1 3 4a1 1 0 0 1 1-1h3.5a1 1 0 0 1 1 1c0 1.25.2 2.45.57 3.6a1 1 0 0 1-.25 1z"/></svg>
        <span>0471 592 304</span>
      </li>
      <li>
        <svg viewBox="0 0 24 24"><path d="M2 5h20v2l-10 6L2 7z"/><path d="M2 9l10 6 10-6v10H2z"/></svg>
        <span>Brent.malvoy@quendix.com.au</span>
      </li>
      <li>
        <svg viewBox="0 0 24 24"><path d="M12 2a7 7 0 0 0-7 7c0 5.2 7 13 7 13s7-7.8 7-13a7 7 0 0 0-7-7zm0 9.5A2.5 2.5 0 1 1 12 6.5a2.5 2.5 0 0 1 0 5z"/></svg>
        <span>87 Harrowgate Ave, Pindarra,<br>QLD, 4000</span>
      </li>
      <li>
        <svg viewBox="0 0 24 24"><path d="M12 2a10 10 0 1 0 0 20 10 10 0 0 0 0-20zm6.9 9h-3a15 15 0 0 0-1.2-5.6A8 8 0 0 1 18.9 11zM12 4.1c.9 1.2 1.8 3.5 2 6.9h-4c.2-3.4 1.1-5.7 2-6.9zM9.3 5.4A15 15 0 0 0 8.1 11h-3a8 8 0 0 1 4.2-5.6zM5.1 13h3a15 15 0 0 0 1.2 5.6A8 8 0 0 1 5.1 13zm6.9 6.9c-.9-1.2-1.8-3.5-2-6.9h4c-.2 3.4-1.1 5.7-2 6.9zm2.7-1.3a15 15 0 0 0 1.2-5.6h3a8 8 0 0 1-4.2 5.6z"/></svg>
        <span>www.quendix.com.au</span>
      </li>
    </ul>
  </section>
  <section class="card card-back">
    <div class="brand"><span class="brand-square"></span>QUENDIX</div>
  </section>
</main>
</body>
</html>
```